Corvane Supplies Business Card

Professional business card that stand out to our potential customers. Front and back with clean modern design

Industry/Entity Type

Oil and gas

Contact Information for Business Card

Name, address, website , office phone and cell number

Requirements
Must have
• Editable files for each employee

```html
<!DOCTYPE html>
<html lang="en">
<head>
<meta charset="utf-8">
<title>Corvane Supplies Business Card</title>
<link href="https://fonts.googleapis.com/css2?family=Didact+Gothic&display=swap" rel="stylesheet">
<style>
  :root {
    --bg: #e4e5e7;
    --card: #04031f;
    --red: #e8252d;
    --cyan: #22b4d2;
    --white: #f2f2f5;
    --faint: rgba(255,255,255,0.05);
  }
  * { margin: 0; padding: 0; box-sizing: border-box; }
  html, body { width: 1200px; height: 800px; overflow: hidden; }
  body {
    background: var(--bg);
    font-family: "Didact Gothic", "Century Gothic", sans-serif;
    display: flex;
    align-items: center;
    justify-content: center;
    gap: 40px;
  }
  .card {
    position: relative;
    width: 540px;
    height: 309px;
    background: var(--card);
    overflow: hidden;
  }
  .brand {
    position: absolute;
    display: flex;
    align-items: center;
    gap: 10px;
    color: var(--red);
    font-size: 22px;
    letter-spacing: 0.06em;
    text-transform: uppercase;
    white-space: nowrap;
  }
  .brand-mark {
    width: 18px;
    height: 18px;
    background: var(--cyan);
  }
  .card-front .brand { left: 150px; top: 108px; font-size: 26px; }
  .card-front .brand .brand-mark { width: 22px; height: 22px; }
  .faint-block {
    position: absolute;
    width: 110px;
    height: 110px;
    background: var(--faint);
  }
  .card-front .faint-block { right: 70px; bottom: 30px; }
  .card-back .faint-block { right: 40px; bottom: 40px; }
  .person { position: absolute; left: 44px; top: 40px; }
  .person-name {
    color: var(--red);
    font-size: 17px;
    letter-spacing: 0.03em;
    text-transform: uppercase;
  }
  .person-role { color: var(--cyan); font-size: 14px; margin-top: 2px; }
  .contact-list {
    position: absolute;
    left: 44px;
    top: 108px;
    list-style: none;
  }
  .contact-list li {
    display: flex;
    align-items: center;
    gap: 9px;
    color: var(--white);
    font-size: 13.5px;
    line-height: 23px;
  }
  .contact-list svg { width: 12px; height: 12px; flex: none; }
  .divider {
    position: absolute;
    left: 175px;
    right: 30px;
    top: 92px;
    height: 1px;
    background: var(--cyan);
    opacity: 0.7;
  }
  .card-back .brand { right: 36px; top: 130px; font-size: 18px; }
</style>
</head>
<body>
  <section class="card card-front" aria-label="Business card front">
    <div class="brand"><span class="brand-mark"></span>Corvane Supplies</div>
    <div class="faint-block" aria-hidden="true"></div>
  </section>

  <section class="card card-back" aria-label="Business card back">
    <div class="person">
      <p class="person-name">Dana Whitlock</p>
      <p class="person-role">Director</p>
    </div>
    <div class="divider"></div>
    <ul class="contact-list">
      <li><svg viewBox="0 0 12 12" fill="none" stroke="#e8252d" stroke-width="1.3"><rect x="3" y="0.8" width="6" height="10.4" rx="1"/><line x1="5" y1="9.3" x2="7" y2="9.3"/></svg>300-555-0142</li>
      <li><svg viewBox="0 0 12 12" fill="#e8252d"><path d="M2.5 1l2 2.2-1 1.3a6.5 6.5 0 0 0 4 4l1.3-1 2.2 2-1.3 1.5C5 10.8 1.2 7 .9 2.3z"/></svg>(832)555-0187</li>
      <li><svg viewBox="0 0 12 12" fill="none" stroke="#e8252d" stroke-width="1.3"><rect x="0.8" y="2.3" width="10.4" height="7.4"/><polyline points="0.8,2.3 6,6.6 11.2,2.3"/></svg>sales@corvanesupplies.com</li>
      <li><svg viewBox="0 0 12 12" fill="none" stroke="#e8252d" stroke-width="1.1"><circle cx="6" cy="6" r="5"/><ellipse cx="6" cy="6" rx="2.2" ry="5"/><line x1="1" y1="6" x2="11" y2="6"/></svg>www.corvanesupplies.com</li>
      <li><svg viewBox="0 0 12 12" fill="#e8252d"><path d="M6 .5a3.8 3.8 0 0 1 3.8 3.8C9.8 7 6 11.5 6 11.5S2.2 7 2.2 4.3A3.8 3.8 0 0 1 6 .5zm0 2.3a1.5 1.5 0 1 0 0 3 1.5 1.5 0 0 0 0-3z"/></svg>418 S.Harlow Ave Suite 3, Midland, Tx 79701</li>
    </ul>
    <div class="brand"><span class="brand-mark"></span>Corvane Supplies</div>
    <div class="faint-block" aria-hidden="true"></div>
  </section>
</body>
</html>
```